Executive Powerpoint

A profession presentation with information consumed at a glance. The data is not relevant, just the design. I have an example attached. The components should be the same but the design improved.

Target Market(s)

The company is Learning Pathways, LLC. We do these presentations for school districts after we build an in-depth report. This is what they use to present the findings to their board.

Industry/Entity Type

Education-School Districts administration level

```html
<!DOCTYPE html>
<html lang="en">
<head>
<meta charset="utf-8">
<title>Learning Pathways, LLC – Executive Presentation</title>
<link href="https://fonts.googleapis.com/css2?family=Manrope:wght@400;500;600;700&display=swap" rel="stylesheet">
<style>
:root{
  --bg:#a1a2a6;
  --green:#a3c63f;
  --ink:#111;
  --text:#2a2a2a;
  --rust:#a9452f;
  --navy:#262b4a;
  --purple:#7a2a9c;
  --blue:#4a87cf;
  --gray:#8a8a8a;
}
*{box-sizing:border-box;margin:0;padding:0}
html,body{width:1025px;height:1200px;overflow:hidden}
body{background:var(--bg);font-family:"Manrope",sans-serif;color:var(--text);position:relative}
.slide{position:absolute;width:437px;height:246px;background:#fff;overflow:hidden}
.col-l{left:64px}.col-r{left:537px}
.row1{top:57px}.row2{top:331px}.row3{top:604px}.row4{top:878px}
.abs{position:absolute}
.logo{position:absolute;display:flex;align-items:center;gap:4px;font-weight:600;color:var(--ink);line-height:1.05}
.logo .dot{border:1.5px solid var(--green);border-radius:50%;flex:none}
.logo.sm{font-size:8.5px}.logo.sm .dot{width:13px;height:13px}
.logo.md{font-size:11px}.logo.md .dot{width:17px;height:17px}
.divider{position:absolute;width:1px;background:#333}
.heading{position:absolute;font-weight:600;font-size:18px;color:var(--ink)}
.heading.green{color:var(--green)}
.photo{position:absolute;background:linear-gradient(135deg,#5d6a6b,#3a3f44 55%,#7b6a5a)}
.photo.desk{background:linear-gradient(135deg,#c7a476,#9e7447 55%,#d8d6d0)}
.small{font-size:6.2px;line-height:1.55}
.cover-title{position:absolute;left:24px;top:96px;font-weight:600;font-size:20px;line-height:1.25;color:var(--ink)}
.cover-title span{color:var(--green)}
.contents-head{position:absolute;left:0;top:0;width:437px;height:52px;box-shadow:0 2px 4px rgba(0,0,0,.06)}
.circ{position:absolute;width:61px;height:61px;border:1px solid var(--green);border-radius:50%;display:flex;align-items:center;justify-content:center}
.clabel{position:absolute;font-size:6.8px;color:var(--text);line-height:1.5}
.table-frame{position:absolute;left:14px;top:57px;width:410px;height:178px;border:4px solid var(--green);background:var(--green)}
.t-head{height:25px;background:#e6e6e6;position:relative}
.t-row{height:24px;background:#fff;position:relative;font-size:7.6px;font-weight:500;color:var(--ink)}
.t-state{height:9px;position:relative;font-size:4.4px;color:#fff;font-weight:700}
.c{position:absolute;top:50%;transform:translateY(-50%)}
.yr{font-size:10px;font-weight:600;color:#3d4a1c}
.card{position:absolute;top:58px;width:199px;height:130px;background:#fff;box-shadow:0 1px 4px rgba(0,0,0,.12)}
.card-title{text-align:center;font-size:7px;font-weight:500;color:var(--ink);margin-top:10px;line-height:1.5}
.legend{position:absolute;left:8px;top:46px;font-size:4.5px;color:#333}
.legend div{display:flex;align-items:center;gap:3px;height:15px}
.legend i{display:block;width:6px;height:6px}
.bars{position:absolute;left:30px;top:44px;width:152px;height:86px;display:flex;justify-content:space-between}
.bar{width:25px;height:85px;display:flex;flex-direction:column;position:relative}
.bar b{display:block}
.bar .v{position:absolute;top:-9px;width:100%;text-align:center;font-size:4.8px}
.bar .y{position:absolute;bottom:-10px;width:100%;text-align:center;font-size:5px}
.s-row{position:absolute;left:16px;display:flex;align-items:center;width:410px}
.s-row .pct{font-size:11px;font-weight:500;color:var(--green);width:44px;margin-left:8px}
.s-row .txt{font-size:6.3px;line-height:1.45;color:var(--ink)}
.box{position:absolute;width:205px;height:52px;background:#f3f3f4;display:flex;align-items:center;padding-left:8px;gap:9px}
.box .ic{width:26px;height:26px;border-radius:50%;background:var(--green);flex:none;display:flex;align-items:center;justify-content:center}
.box p{font-size:6.3px;line-height:1.45;color:var(--ink)}
.thanks{background:linear-gradient(135deg,#a8cc45,#9cc13a 60%,#a6c944)}
</style>
</head>
<body>

<section class="slide col-l row1" aria-label="Cover">
  <div class="logo md" style="left:22px;top:27px"><span class="dot"></span><span>Learning<br>Pathways, LLC</span></div>
  <h1 class="cover-title"><span>MAPLECREST</span><br>SCHOOL<br>DISTRICT</h1>
  <p class="abs small" style="left:24px;top:176px;width:140px;font-size:6.8px;color:var(--ink)">Lorem Ipsum is simply dummy text of the printing and typesetting industry</p>
  <div class="photo" style="left:206px;top:0;width:231px;height:246px" role="img" aria-label="Photo of hands typing on a laptop showing a data dashboard"></div>
</section>

<section class="slide col-r row1" style="top:55px" aria-label="Contents">
  <div class="contents-head"></div>
  <div class="logo sm" style="left:10px;top:13px"><span class="dot"></span><span>Learning<br>Pathways, LLC</span></div>
  <div class="divider" style="left:99px;top:11px;height:29px"></div>
  <div class="heading green" style="left:115px;top:8px;font-size:15px">Contents</div>
  <p class="abs" style="left:116px;top:30px;font-size:6.2px;color:var(--ink)">Lorem Ipsum is simply dummy text of the printing and typesetting industry</p>

  <div class="circ" style="left:18px;top:71px"><svg width="24" height="24" viewBox="0 0 24 24" fill="none" stroke="#a3c63f" stroke-width="1.2"><rect x="4" y="9" width="16" height="11"/><path d="M6 9V4h12v5M4 13h16M9 16h6"/></svg></div>
  <div class="clabel" style="left:90px;top:98px">Introduction</div>
  <div class="circ" style="left:158px;top:71px"><svg width="24" height="24" viewBox="0 0 24 24" fill="none" stroke="#a3c63f" stroke-width="1.2"><rect x="5" y="4" width="14" height="17" rx="1"/><path d="M9 3h6v3H9zM8 10h1M11 10h5M8 14h1M11 14h5M8 18h1M11 18h5"/></svg></div>
  <div class="clabel" style="left:231px;top:98px">Accountability</div>
  <div class="circ" style="left:303px;top:71px"><svg width="24" height="24" viewBox="0 0 24 24" fill="none" stroke="#a3c63f" stroke-width="1.2"><rect x="4" y="3" width="13" height="17"/><circle cx="12" cy="12" r="4"/><path d="M15 15l5 5"/></svg></div>
  <div class="clabel" style="left:375px;top:98px">Assessment</div>

  <div class="clabel" style="left:41px;top:171px">Enrollment/<br>Attendance</div>
  <div class="circ" style="left:92px;top:151px"><svg width="24" height="24" viewBox="0 0 24 24" fill="none" stroke="#a3c63f" stroke-width="1.2"><path d="M6 3h8l4 4v13H6z"/><path d="M9 10h6M9 13h4"/><circle cx="17" cy="18" r="3"/><path d="M17 16.5v3M15.5 18h3"/></svg></div>
  <div class="clabel" style="left:192px;top:179px">Survey</div>
  <div class="circ" style="left:224px;top:151px"><svg width="24" height="24" viewBox="0 0 24 24" fill="none" stroke="#a3c63f" stroke-width="1.2"><rect x="4" y="4" width="13" height="17"/><path d="M7 8h3v3H7zM7 14h3v3H7zM12 9h3M12 15h2M14 19l6-9 1 1-6 9z"/></svg></div>
  <div class="clabel" style="left:316px;top:179px">Schools</div>
  <div class="circ" style="left:351px;top:151px"><svg width="24" height="24" viewBox="0 0 24 24" fill="none" stroke="#a3c63f" stroke-width="1.2"><path d="M3 20h18M5 20v-8h14v8M8 12l4-4 4 4M12 8V3h3M10 20v-4h4v4M7 15h1M16 15h1"/></svg></div>
</section>

<section class="slide col-l row2" aria-label="Introduction">
  <div class="logo sm" style="left:18px;top:18px"><span class="dot"></span><span>Learning<br>Pathways, LLC</span></div>
  <div class="heading green" style="left:19px;top:60px;font-size:21px">Introduction</div>
  <p class="abs small" style="left:19px;top:92px;width:182px;color:var(--ink)">Sed ut perspiciatis unde omnis iste natus error sit volu ptatem accusantium doloremque laudantium, totam rem aperiam, eaque ipsa quae ab illo inventore veritatis et quasi architecto beatae vitae dicta sunt explicabo. Nemo enim ipsam voluptatem quia voluptas sit aspernatur aut odit aut fugit, sed quia consequuntur magni dolores eos qui ratione voluptatem sequi nesciunt. Neque porro quisquam est, qui dolorem ipsum quia dolor sit amet, consectetur, adipisci velit, sed quia non numquam eius modi tempora incidunt ut labore et dolore magnam aliquam quaerat voluptatem. Ut enim ad minima veniam, quis nostrum exercitationem ullam corporis suscipit laboriosam, nisi ut aliquid</p>
  <div class="photo desk" style="left:219px;top:0;width:218px;height:246px" role="img" aria-label="Overhead photo of a wooden desk with printed charts, a calculator and hands pointing with a pen"></div>
</section>

<section class="slide col-r row2" aria-label="Accountability">
  <div class="logo sm" style="left:14px;top:16px"><span class="dot"></span><span>Learning<br>Pathways, LLC</span></div>
  <div class="divider" style="left:100px;top:12px;height:29px"></div>
  <div class="heading green" style="left:112px;top:15px;font-size:19px">Accountability</div>
  <div class="table-frame">
    <div class="t-head">
      <span class="c yr" style="left:182px">2018</span>
      <span class="c yr" style="left:261px">2019</span>
      <span class="c yr" style="left:341px">2021</span>
    </div>
    <div style="height:3px;background:#fff"></div>
    <div class="t-row"><span class="c" style="left:16px">ELA/LANG. ARTS</span><span class="c" style="left:181px">18.9%</span><svg class="c" style="left:227px" width="12" height="12" viewBox="0 0 12 12"><path d="M6 1l5 5H8v5H4V6H1z" fill="#5a9c84"/></svg><span class="c" style="left:262px">19.1%</span><svg class="c" style="left:309px" width="12" height="12" viewBox="0 0 12 12"><path d="M6 11l5-5H8V1H4v5H1z" fill="#d9553a"/></svg><span class="c" style="left:341px">18.9%</span></div>
    <div class="t-state" style="background:var(--rust)"><span class="c" style="left:147px">STATE</span><span class="c" style="left:182px">39.8%</span><span class="c" style="left:266px">41.8%</span><span class="c" style="left:343px">35.0%</span></div>
    <div class="t-row"><span class="c" style="left:16px">MATH</span><span class="c" style="left:181px">16.1%</span><svg class="c" style="left:227px" width="12" height="12" viewBox="0 0 12 12"><path d="M6 1l5 5H8v5H4V6H1z" fill="#5a9c84"/></svg><span class="c" style="left:262px">18.5%</span><svg class="c" style="left:309px" width="12" height="12" viewBox="0 0 12 12"><path d="M6 11l5-5H8V1H4v5H1z" fill="#d9553a"/></svg><span class="c" style="left:341px">16.1%</span></div>
    <div class="t-state" style="background:var(--navy)"><span class="c" style="left:147px">STATE</span><span class="c" style="left:182px">39.8%</span><span class="c" style="left:266px">41.8%</span><span class="c" style="left:343px">35.0%</span></div>
    <div class="t-row"><span class="c" style="left:16px">SCIENCE</span><span class="c" style="left:181px">36.1%</span><svg class="c" style="left:227px" width="12" height="12" viewBox="0 0 12 12"><path d="M6 11l5-5H8V1H4v5H1z" fill="#d9553a"/></svg><span class="c" style="left:262px">24.8%</span><svg class="c" style="left:309px" width="12" height="12" viewBox="0 0 12 12"><path d="M6 11l5-5H8V1H4v5H1z" fill="#d9553a"/></svg><span class="c" style="left:341px">36.1%</span></div>
    <div class="t-state" style="background:var(--green)"><span class="c" style="left:147px">STATE</span><span class="c" style="left:182px">39.8%</span><span class="c" style="left:266px">41.8%</span><span class="c" style="left:343px">35.0%</span></div>
    <div class="t-row"><span class="c" style="left:16px">U.S. HISTORY</span><span class="c" style="left:181px">26.9%</span><svg class="c" style="left:227px" width="12" height="12" viewBox="0 0 12 12"><path d="M6 1l5 5H8v5H4V6H1z" fill="#5a9c84"/></svg><span class="c" style="left:262px">27.0%</span><svg class="c" style="left:309px" width="12" height="12" viewBox="0 0 12 12"><path d="M6 11l5-5H8V1H4v5H1z" fill="#d9553a"/></svg><span class="c" style="left:341px">26.9%</span></div>
    <div class="t-state" style="background:var(--green)"><span class="c" style="left:147px">STATE</span><span class="c" style="left:182px">39.8%</span><span class="c" style="left:266px">41.8%</span><span class="c" style="left:343px">35.0%</span></div>
    <div style="height:4px;background:#fff"></div>
  </div>
</section>

<section class="slide col-l row3" aria-label="Science assessment">
  <div class="abs" style="left:356px;top:-62px;width:140px;height:140px;border-radius:50%;background:var(--green)"></div>
  <div class="abs" style="left:375px;top:21px;font-size:13px;font-weight:500;color:#fff">SCIENCE</div>
  <div class="logo sm" style="left:14px;top:16px"><span class="dot"></span><span>Learning<br>Pathways, LLC</span></div>
  <div class="divider" style="left:102px;top:12px;height:29px"></div>
  <div class="heading" style="left:115px;top:14px;font-size:18px">LPA-SCI</div>

  <div class="card" style="left:14px">
    <div class="card-title">MAPLECREST SCHOOL DISTRICT<br>LPA-SCI GRADE 5</div>
    <div class="legend"><div><i style="background:var(--gray)"></i>5</div><div><i style="background:var(--green)"></i>4</div><div><i style="background:var(--navy)"></i>3</div><div><i style="background:var(--purple)"></i>2</div><div><i style="background:var(--blue)"></i>1</div></div>
    <div class="bars">
      <div class="bar"><span class="v">30.7</span><b style="flex:12;background:var(--gray)"></b><b style="flex:4;background:var(--green)"></b><b style="flex:25;background:var(--navy)"></b><b style="flex:45;background:var(--purple)"></b><b style="flex:60;background:var(--blue)"></b><span class="y">2019</span></div>
      <div class="bar"><span class="v">23.5</span><b style="flex:12;background:var(--gray)"></b><b style="flex:22;background:var(--green)"></b><b style="flex:20;background:var(--navy)"></b><b style="flex:32;background:var(--purple)"></b><b style="flex:60;background:var(--blue)"></b><span class="y">2020</span></div>
      <div class="bar"><span class="v">18.9</span><b style="flex:12;background:var(--gray)"></b><b style="flex:4;background:var(--green)"></b><b style="flex:25;background:var(--navy)"></b><b style="flex:45;background:var(--purple)"></b><b style="flex:60;background:var(--blue)"></b><span class="y">2021</span></div>
      <div class="bar"><span class="v">8.8</span><b style="flex:12;background:var(--gray)"></b><b style="flex:22;background:var(--green)"></b><b style="flex:20;background:var(--navy)"></b><b style="flex:32;background:var(--purple)"></b><b style="flex:60;background:var(--blue)"></b><span class="y">2022</span></div>
    </div>
  </div>
  <div class="card" style="left:228px">
    <div class="card-title">MAPLECREST SCHOOL DISTRICT<br>LPA-SCI GRADE 8</div>
    <div class="legend"><div><i style="background:var(--gray)"></i>5</div><div><i style="background:var(--green)"></i>4</div><div><i style="background:var(--navy)"></i>3</div><div><i style="background:var(--purple)"></i>2</div><div><i style="background:var(--blue)"></i>1</div></div>
    <div class="bars">
      <div class="bar"><span class="v">30.7</span><b style="flex:12;background:var(--gray)"></b><b style="flex:4;background:var(--green)"></b><b style="flex:25;background:var(--navy)"></b><b style="flex:45;background:var(--purple)"></b><b style="flex:60;background:var(--blue)"></b><span class="y">2019</span></div>
      <div class="bar"><span class="v">23.5</span><b style="flex:12;background:var(--gray)"></b><b style="flex:22;background:var(--green)"></b><b style="flex:20;background:var(--navy)"></b><b style="flex:32;background:var(--purple)"></b><b style="flex:60;background:var(--blue)"></b><span class="y">2020</span></div>
      <div class="bar"><span class="v">18.9</span><b style="flex:12;background:var(--gray)"></b><b style="flex:4;background:var(--green)"></b><b style="flex:25;background:var(--navy)"></b><b style="flex:45;background:var(--purple)"></b><b style="flex:60;background:var(--blue)"></b><span class="y">2021</span></div>
      <div class="bar"><span class="v">8.8</span><b style="flex:12;background:var(--gray)"></b><b style="flex:22;background:var(--green)"></b><b style="flex:20;background:var(--navy)"></b><b style="flex:32;background:var(--purple)"></b><b style="flex:60;background:var(--blue)"></b><span class="y">2022</span></div>
    </div>
  </div>
  <p class="abs" style="left:0;top:213px;width:437px;text-align:center;font-size:6.9px;line-height:1.6;color:var(--ink)">Science proficiency in the 5th grade grew by 3.8 percentage points between 2019 and 2021 despite the pandemic.<br>Science proficiency declined slightly (1.6 points) for eighth-graders over the same period.</p>
</section>

<section class="slide col-r row3" aria-label="Survey">
  <div class="logo sm" style="left:14px;top:16px"><span class="dot"></span><span>Learning<br>Pathways, LLC</span></div>
  <div class="divider" style="left:102px;top:12px;height:29px"></div>
  <div class="heading" style="left:115px;top:14px;font-size:18px">Survey</div>
  <div class="s-row" style="top:57px"><svg width="16" height="16" viewBox="0 0 24 24" fill="none" stroke="#a3c63f" stroke-width="1.6"><path d="M12 3l7 3v6c0 4-3 7-7 9-4-2-7-5-7-9V6z"/><path d="M9 12l2 2 4-4"/></svg><span class="pct">77.9 %</span><span class="txt">Lorem ipsum dolor sit amet, consectetur adipiscing elit</span></div>
  <div class="s-row" style="top:84px"><svg width="16" height="16" viewBox="0 0 24 24" fill="none" stroke="#a3c63f" stroke-width="1.6"><rect x="5" y="3" width="14" height="18"/><path d="M8 16v2M11 13v5M14 10v8"/></svg><span class="pct">82.0%</span><span class="txt">Sed ut perspiciatis unde omnis iste natus error sit voluptatem accusantium doloremque<br>laudantium, totam rem aperiam, eaque ipsa quae ab illo inventore</span></div>
  <div class="s-row" style="top:118px"><svg width="16" height="16" viewBox="0 0 24 24" fill="none" stroke="#a3c63f" stroke-width="1.6"><path d="M3 6c3-1 6-1 9 1 3-2 6-2 9-1v13c-3-1-6-1-9 1-3-2-6-2-9-1zM12 7v13"/></svg><span class="pct">36.0%</span><span class="txt">At vero eos et accusamus et iusto odio dignissimos ducimus qui blanditiis praesentium voluptatum<br>deleniti atque corrupti quos dolores et quas molestias exceptur</span></div>
  <div class="s-row" style="top:150px"><svg width="16" height="16" viewBox="0 0 24 24" fill="none" stroke="#a3c63f" stroke-width="1.6"><path d="M6 3h9l3 3v15H6z"/><path d="M9 9h6M9 12h6M9 15h3M14 20l5-6 1.5 1.5-5 6z"/></svg><span class="pct">77.9 %</span><span class="txt">Lorem ipsum dolor sit amet, consectetur adipiscing elit</span></div>
  <div class="s-row" style="top:177px"><svg width="16" height="16" viewBox="0 0 24 24" fill="none" stroke="#a3c63f" stroke-width="1.6"><circle cx="12" cy="12" r="9"/><path d="M3 12h18M12 3c3 3 3 15 0 18M12 3c-3 3-3 15 0 18"/></svg><span class="pct">82.0%</span><span class="txt">Sed ut perspiciatis unde omnis iste natus error sit voluptatem accusantium doloremque<br>laudantium, totam rem aperiam, eaque ipsa quae ab illo inventore</span></div>
  <div class="s-row" style="top:211px"><svg width="16" height="16" viewBox="0 0 24 24" fill="none" stroke="#a3c63f" stroke-width="1.6"><circle cx="10" cy="10" r="7"/><path d="M15 15l6 6M7 11l2 2 4-4"/></svg><span class="pct">36.0%</span><span class="txt">Sed ut perspiciatis unde omnis iste natus error sit voluptatem accusantium doloremque<br>laudantium, totam rem aperiam, eaque ipsa quae ab illo inventore</span></div>
</section>

<section class="slide col-l row4" aria-label="Maplecrest High">
  <div class="logo sm" style="left:14px;top:16px"><span class="dot"></span><span>Learning<br>Pathways, LLC</span></div>
  <div class="divider" style="left:102px;top:12px;height:29px"></div>
  <div class="heading" style="left:115px;top:14px;font-size:18px">Maplecrest High</div>
  <div class="box" style="left:12px;top:57px"><span class="ic"><svg width="15" height="15" viewBox="0 0 24 24" fill="none" stroke="#222" stroke-width="1.8"><path d="M2 9l10-5 10 5-10 5zM6 11v5c3 2 9 2 12 0v-5"/></svg></span><p>Sed ut perspiciatis unde omnis iste natus error<br>sit voluptatem accusantium doloremque<br>laudantium, totam rem aperiam.</p></div>
  <div class="box" style="left:224px;top:57px"><span class="ic"><svg width="15" height="15" viewBox="0 0 24 24" fill="none" stroke="#222" stroke-width="1.8"><circle cx="9" cy="14" r="4"/><circle cx="16" cy="7" r="3"/></svg></span><p>On the other hand, we denounce with righte<br>ous indignation and dislike men who are so<br>beguiled and demoralized by the charms.</p></div>
  <div class="box" style="left:12px;top:119px"><span class="ic"><svg width="15" height="15" viewBox="0 0 24 24" fill="none" stroke="#222" stroke-width="1.8"><path d="M3 7c3-1 6-1 9 1 3-2 6-2 9-1v12c-3-1-6-1-9 1-3-2-6-2-9-1zM12 8v12"/></svg></span><p>Sed ut perspiciatis unde omnis iste natus error<br>sit voluptatem accusantium doloremque<br>laudantium, totam rem aperiam.</p></div>
  <div class="box" style="left:224px;top:119px"><span class="ic"><svg width="15" height="15" viewBox="0 0 24 24" fill="none" stroke="#222" stroke-width="1.8"><circle cx="12" cy="9" r="5"/><path d="M12 14v7M8 21h8"/></svg></span><p>On the other hand, we denounce with righte<br>ous indignation and dislike men who are so<br>beguiled and demoralized by the charms.</p></div>
  <div class="box" style="left:12px;top:181px"><span class="ic"><svg width="15" height="15" viewBox="0 0 24 24" fill="none" stroke="#222" stroke-width="1.8"><rect x="4" y="4" width="16" height="12"/><path d="M8 20h8M12 16v4"/></svg></span><p>Sed ut perspiciatis unde omnis iste natus error<br>sit voluptatem accusantium doloremque<br>laudantium, totam rem aperiam.</p></div>
  <div class="box" style="left:224px;top:181px"><span class="ic"><svg width="15" height="15" viewBox="0 0 24 24" fill="none" stroke="#222" stroke-width="1.8"><path d="M6 3h9l3 3v15H6z"/><path d="M9 9h6M9 13h6"/></svg></span><p>On the other hand, we denounce with righte<br>ous indignation and dislike men who are so<br>beguiled and demoralized by the charms.</p></div>
</section>

<section class="slide col-r row4 thanks" style="top:883px" aria-label="Thank you">
  <div class="logo" style="left:150px;top:22px;font-size:15px;font-weight:600;color:var(--ink)"><span class="dot" style="width:24px;height:24px;border-color:#fff"></span><span>Learning<br>Pathways, LLC</span></div>
  <div class="abs" style="left:148px;top:104px;width:146px;height:1px;background:#333"></div>
  <div class="abs" style="left:0;top:113px;width:437px;text-align:center;font-size:25px;font-weight:600;color:var(--ink)">Thank You</div>
  <div class="abs" style="left:148px;top:150px;width:146px;height:1px;background:#333"></div>
  <svg class="abs" style="left:208px;top:180px" width="21" height="21" viewBox="0 0 24 24" fill="none" stroke="#222" stroke-width="1"><circle cx="12" cy="12" r="11"/><rect x="7" y="8.5" width="10" height="7"/><path d="M7 8.5l5 4 5-4"/></svg>
  <div class="abs" style="left:0;top:206px;width:437px;text-align:center;font-size:7.8px;font-weight:500;line-height:1.7;color:var(--ink)">Email us<br>hello@learningpathways-demo.com</div>
</section>

</body>
</html>
```